MERROWGATE WINE LABEL RANGE PROJECT

We need an elegant wine label design for our new range of wine. We need 3 labels for the range

2015 Merrowgate Shiraz
2015 Merrowgate Cabernet
2015 Merrowgate Shiraz Cabernet

The Size is nominated at 120mm High x 70mm Wide (Front and Back) but we are open to creative expression even if size differs

We are open to any style of label and designer can work on their strengths. it can be modern/classic/old fashion etc

I will attach the tasting notes which shows the title of wine for front label and tasting notes and details to be included at back. Please leave space for a barcode.

Thanks
Tamir.

Target Market(s)

WINE DRINKERS 35-65

Requirements
Must have
• ELEGANCE

```html
<!DOCTYPE html>
<html lang="en">
<head>
<meta charset="utf-8">
<title>Merrowgate Wine Label Range</title>
<link href="https://fonts.googleapis.com/css2?family=EB+Garamond:wght@400;500&display=swap" rel="stylesheet">
<style>
  :root {
    --backdrop: #7a7a7a;
    --label-black: #151515;
    --label-black-edge: #0b0b0b;
    --paper: #f1f1ef;
    --ink: #1d1d1d;
    --brand-gold: #c9a24a;
    --gold-deep: #a8832c;
    --gold-light: #efe1a2;
    --red-deep: #8c0f18;
    --red-light: #e2323c;
    --blue-deep: #3a2f8f;
    --blue-light: #7f86e0;
  }
  * { margin: 0; padding: 0; box-sizing: border-box; }
  html, body { width: 886px; height: 1200px; overflow: hidden; }
  body {
    background: radial-gradient(ellipse at 50% 40%, #858585 0%, var(--backdrop) 70%);
    font-family: "EB Garamond", Georgia, serif;
  }
  .label-range {
    width: 886px; height: 1200px;
    display: flex; justify-content: space-evenly; align-items: center;
  }
  .label {
    position: relative;
    width: 240px; height: 408px;
    box-shadow: 0 6px 18px rgba(0,0,0,0.35);
  }
  .label__art { position: absolute; inset: 0; width: 100%; height: 100%; display: block; }
  .label__brand {
    position: absolute; top: 38px; left: 0; right: 0;
    text-align: center; color: var(--brand-gold);
    font-size: 27px; font-weight: 500; letter-spacing: 0.5px;
  }
  .label__wine {
    position: absolute; top: 330px; left: 0; right: 0;
    text-align: center; color: var(--ink);
    font-size: 19px; line-height: 1.25;
  }
  .label__vintage {
    display: block; margin-top: 6px;
    font-size: 11px; letter-spacing: 2px;
  }
  .label--blend .label__wine { top: 318px; }
  .label--blend .label__vintage { margin-top: 3px; }
</style>
</head>
<body>
<main class="label-range">

  <article class="label label--cabernet">
    <svg class="label__art" viewBox="0 0 240 408" aria-hidden="false">
      <defs>
        <linearGradient id="black-cab" x1="0" y1="0" x2="0" y2="1">
          <stop offset="0" stop-color="var(--label-black)"/>
          <stop offset="1" stop-color="var(--label-black-edge)"/>
        </linearGradient>
        <linearGradient id="tone-gold" x1="0" y1="1" x2="1" y2="0">
          <stop offset="0" stop-color="var(--gold-deep)"/>
          <stop offset="1" stop-color="var(--gold-light)"/>
        </linearGradient>
      </defs>
      <rect width="240" height="408" fill="url(#black-cab)"/>
      <polygon points="0,268 240,214 240,408 0,408" fill="var(--paper)"/>
      <rect x="24" y="176" width="192" height="124" rx="14" fill="url(#tone-gold)" opacity="0.85"
            role="img" aria-label="Large gold script monogram"/>
    </svg>
    <h2 class="label__brand">Merrowgate</h2>
    <p class="label__wine">Merrowgate Cabernet<span class="label__vintage">2015</span></p>
  </article>

  <article class="label label--shiraz">
    <svg class="label__art" viewBox="0 0 240 408">
      <defs>
        <linearGradient id="black-shz" x1="0" y1="0" x2="0" y2="1">
          <stop offset="0" stop-color="var(--label-black)"/>
          <stop offset="1" stop-color="var(--label-black-edge)"/>
        </linearGradient>
        <linearGradient id="tone-red" x1="0" y1="1" x2="1" y2="0">
          <stop offset="0" stop-color="var(--red-deep)"/>
          <stop offset="1" stop-color="var(--red-light)"/>
        </linearGradient>
      </defs>
      <rect width="240" height="408" fill="url(#black-shz)"/>
      <polygon points="0,268 240,214 240,408 0,408" fill="var(--paper)"/>
      <rect x="24" y="176" width="192" height="124" rx="14" fill="url(#tone-red)" opacity="0.9"
            role="img" aria-label="Large red script monogram"/>
    </svg>
    <h2 class="label__brand">Merrowgate</h2>
    <p class="label__wine">Merrowgate Shiraz<span class="label__vintage">2015</span></p>
  </article>

  <article class="label label--blend">
    <svg class="label__art" viewBox="0 0 240 408">
      <defs>
        <linearGradient id="black-bl" x1="0" y1="0" x2="0" y2="1">
          <stop offset="0" stop-color="var(--label-black)"/>
          <stop offset="1" stop-color="var(--label-black-edge)"/>
        </linearGradient>
        <linearGradient id="tone-blue" x1="0" y1="1" x2="1" y2="0">
          <stop offset="0" stop-color="var(--blue-deep)"/>
          <stop offset="1" stop-color="var(--blue-light)"/>
        </linearGradient>
      </defs>
      <rect width="240" height="408" fill="url(#black-bl)"/>
      <polygon points="0,268 240,214 240,408 0,408" fill="var(--paper)"/>
      <rect x="24" y="176" width="192" height="124" rx="14" fill="url(#tone-blue)" opacity="0.9"
            role="img" aria-label="Large violet script monogram"/>
    </svg>
    <h2 class="label__brand">Merrowgate</h2>
    <p class="label__wine">Merrowgate Shiraz<br>Cabernet<span class="label__vintage">2015</span></p>
  </article>

</main>
</body>
</html>
```